Presentation Folder Design Project

We need a folder to be designed, which will be specifically for holding and sharing the different information and collateral to our prospective clients, our partners, and anyone else that would like to learn more about our organization. For this folder you will create and design a 18x12 (When laying open flat), front-to-back as well as inside panels, folder to hold all of our presentation information as well as company collateral. The folder design/shape is going to be very unique. Instead of being a standard folder that opens from right to left, with a fold in the middle of the two halves, this folder will open like two doors in front of the viewer. Essentially, there will be a split down the middle of the front panel with the folds being on both the left and right side of the folder. This will create a left flap and a right flap in the front that will open like French doors and the back of the folder will be one solid panel like a standard folder. On the front flapping ‘doors’ (on the inside of the folder) there will be pockets on the bottom of each flap to hold collateral material like brochures and things of that nature. Additionally, there will be a larger pocket on the bottom of the back panel as well. I would like for there to be a spot where the business card can rest in the middle larger back pocket. It will be centered. This inside panel (or what is essentially the back of the folder after the two front flaps are opened) will also hold different paperwork and company informative material. The overall look I would like to achieve is that the two front flaps are going to be doors opening to the information inside. Kind of like saying “welcome home”, then you open the doors to “walk” inside. Use the 'door' theme in your design.

The folder must demonstrate both attention to detail, sophistication and comfort. Our organization is built around warmth, care and individualized personal attention. The most important aspect of this design is to focus on creating a nurturing, warm, and inviting first impression and feel that would attract a prospective client to want to utilize our services and to feel like they would want to walk through those doors on the front of the folder. They need to want to enter.

I am open to the creativity of the designer to develop something based on the above criteria; however I would like the design to work well with our existing collateral material. What I mean by that is that I want it to look like it is “at home” inside of the folder. Like stylistically it belongs and it fits well with what we have created collateral wide for our other companies.Because of this, I would like for the designer to pull inspiration from the link to our website (Located below) as well as from our recently refreshed business cards, and our 3 company logos (All Attached). This should allow the Folder design to be unique and creative, while still staying inside of a framework and the feel/style that I am looking for.
Updates

There are limited submissions on this design project and I would like to see more. Many more!

Target Market(s)

Seniors(50+), Caring Family Members, Social Workers, Professional or Retired Professional, Affluent, Female

Industry/Entity Type

Business

Requirements
Must have
• • The company logos must be included.

www.harbenhearthteam.example
Nice to have
• I will be contacting individual designers to make adjustments, tweaks, and changes based on a design by design basis. Only designs that demonstrate proximity to my vision will be contacted to make subtle updates to original designs. First impressions are HUGE, both in your designs for me and ultimately my collateral to my clients.

```html
<!DOCTYPE html>
<html lang="en">
<head>
<meta charset="utf-8">
<title>Harben Care Group – Presentation Folder</title>
<link href="https://fonts.googleapis.com/css2?family=Cormorant+Garamond:wght@500;600&family=Crimson+Pro:ital,wght@0,400;0,500;1,400;1,500&family=Open+Sans:wght@400&display=swap" rel="stylesheet">
<style>
  :root{
    --stage-top:#0a2f31;
    --stage-bottom:#133f40;
    --teal-deep:#0f5b5d;
    --teal-mid:#1d6e70;
    --teal-soft:#6ea8aa;
    --teal-pale:#8dbdbe;
    --blush:#f3958d;
    --paper:#ffffff;
    --leaf:#7fae3e;
    --leaf-light:#a8c96a;
    --leaf-dark:#4f7f2a;
    --shirt:#6f9fd6;
    --khaki:#d9cdb4;
    --ink-light:#e9f3f3;
  }
  *{box-sizing:border-box;margin:0;padding:0}
  html,body{width:1200px;height:1000px;overflow:hidden}
  body{
    background:linear-gradient(180deg,var(--stage-top),var(--stage-bottom));
    position:relative;
    font-family:"Crimson Pro",Georgia,serif;
    color:var(--ink-light);
  }
  .panel{position:absolute;overflow:hidden}

  /* ---------- Front cover: two doors ---------- */
  .front-cover{left:260px;top:40px;width:300px;height:400px;display:flex}
  .door{position:relative;width:150px;height:100%;background:var(--teal-deep);overflow:hidden}
  .door + .door{border-left:1px solid #0a4345}
  .door-shape{position:absolute;left:0;top:0;width:100%;height:100%}
  .door-brand{
    position:absolute;left:14px;bottom:30px;display:flex;align-items:center;gap:6px;
    font-family:"Cormorant Garamond",Georgia,serif;font-weight:600;font-size:15px;color:var(--paper);line-height:1.05
  }
  .brand-square{width:16px;height:16px;background:var(--paper);flex:none}
  .door-tagline{
    position:absolute;left:0;right:0;bottom:32px;text-align:center;
    font-style:italic;font-size:12px;line-height:1.2;color:var(--paper)
  }

  /* ---------- Back cover ---------- */
  .back-cover{left:640px;top:40px;width:300px;height:400px;background:var(--teal-deep);text-align:center}
  .back-brand{margin-top:60px;display:flex;flex-direction:column;align-items:center;gap:10px}
  .back-brand .brand-square{width:58px;height:58px;background:var(--blush);border-radius:8px}
  .back-brand-name{font-family:"Cormorant Garamond",Georgia,serif;font-weight:600;font-size:24px;color:var(--paper);line-height:1}
  .partner-row{display:flex;justify-content:center;gap:22px;margin-top:26px}
  .partner-badge{width:22px;height:22px;border:1px solid var(--ink-light);border-radius:3px}
  .contact{margin-top:54px;font-size:8px;line-height:1.45;color:var(--ink-light)}
  .contact .web{margin-top:8px;font-size:10px;font-weight:500;color:var(--paper)}

  /* ---------- Inside spread ---------- */
  .inside-spread{left:225px;top:470px;width:750px;height:500px;display:flex}
  .flap{position:relative;width:187.5px;height:100%;background:var(--teal-mid)}
  .flap-left{border-right:1px solid #0a4345}
  .flap-right{border-left:1px solid #0a4345}
  .insert{position:absolute;left:10px;right:10px;top:14px;height:300px;background:var(--paper);overflow:hidden}
  .pocket{position:absolute;left:0;right:0;bottom:0;height:210px;background:var(--teal-deep)}
  .pocket-left{clip-path:polygon(0 14%,100% 0,100% 100%,0 100%)}
  .pocket-right{clip-path:polygon(0 0,100% 14%,100% 100%,0 100%)}
  .card-slot{
    position:absolute;left:50%;top:58px;width:100px;height:62px;margin-left:-50px;
    background:var(--teal-pale);
    clip-path:polygon(12% 0,88% 0,100% 25%,100% 75%,88% 100%,12% 100%,0 75%,0 25%);
    display:flex;align-items:center;justify-content:center;text-align:center;
    font-family:"Open Sans",Arial,sans-serif;font-size:11px;line-height:1.2;color:var(--teal-deep)
  }

  /* left insert */
  .insert-banner{height:70px;background:linear-gradient(90deg,#8a6a4e,#a9c27b 40%,#cfe0a6)}
  .insert-banner span{display:block;padding:10px 0 0 58px;font-family:"Cormorant Garamond",Georgia,serif;font-size:12px;color:var(--paper);line-height:1.8}
  .insert-brand{display:flex;align-items:center;gap:6px;padding:14px 12px 0;font-family:"Cormorant Garamond",Georgia,serif;font-weight:600;font-size:18px;color:var(--teal-deep)}
  .insert-brand .brand-square{background:var(--teal-deep);width:18px;height:18px}
  .insert-tagline{padding:8px 12px 0;font-style:italic;font-size:11px;line-height:1.25;color:var(--blush)}
  .insert-bar{margin:10px 12px 0;height:14px;background:var(--teal-deep)}
  .insert-copy{padding:8px 12px 0;font-size:10px;line-height:1.3;color:#333}

  /* right insert */
  .insert-right .insert-head{display:flex;align-items:center;gap:6px;padding:14px 12px;font-family:"Cormorant Garamond",Georgia,serif;font-weight:600;font-size:18px;color:var(--teal-deep)}
  .insert-right .insert-head .brand-square{background:var(--teal-deep);width:18px;height:18px}
  .insert-right .insert-band{background:var(--teal-deep);padding:10px 8px;text-align:center;font-style:italic;font-size:11px;line-height:1.25;color:var(--paper)}
  .insert-photo{position:absolute;left:0;right:0;bottom:0;height:170px;background:linear-gradient(160deg,#9cbf6a,#c97a8e 55%,#6f8f4a)}

  /* center back panel */
  .center{position:relative;width:375px;height:100%}
  .hero-photo{
    position:absolute;inset:0;
    background:linear-gradient(180deg,var(--leaf-light) 0%,var(--leaf) 22%,#7a9cc4 42%,var(--shirt) 58%,var(--khaki) 78%,var(--leaf-dark) 100%);
  }
  .hero-tagline{
    position:absolute;left:0;right:0;top:258px;text-align:center;
    font-style:italic;font-size:30px;line-height:1.15;color:var(--paper);
    text-shadow:0 1px 3px rgba(0,0,0,.4)
  }
</style>
</head>
<body>

  <!-- Front cover -->
  <section class="panel front-cover" aria-label="Folder front, two doors">
    <div class="door door-left">
      <svg class="door-shape" viewBox="0 0 150 400" preserveAspectRatio="none" aria-hidden="true">
        <path d="M0 0H150V232Q75 205 0 222Z" fill="var(--teal-soft)"/>
      </svg>
      <div class="door-brand"><span class="brand-square"></span><span>Harben<br>Care Group</span></div>
    </div>
    <div class="door door-right">
      <svg class="door-shape" viewBox="0 0 150 400" preserveAspectRatio="none" aria-hidden="true">
        <path d="M0 0H150V222Q75 205 0 232Z" fill="var(--teal-soft)"/>
      </svg>
      <p class="door-tagline">Someone you can depend on...<br>Without question.</p>
    </div>
  </section>

  <!-- Back cover -->
  <section class="panel back-cover" aria-label="Folder back">
    <div class="back-brand">
      <span class="brand-square"></span>
      <span class="back-brand-name">Harben<br>Care Group</span>
    </div>
    <div class="partner-row">
      <span class="partner-badge"></span>
      <span class="partner-badge"></span>
    </div>
    <div class="contact">
      <p>120 Harbor Lane, Suite 4, Fairview, IL 60000</p>
      <p>Phone 555-010-0100 · Fax 555-010-0101</p>
      <p>Email: info@harbenhearthteam.example</p>
      <p class="web">www.harbenhearthteam.example</p>
    </div>
  </section>

  <!-- Inside spread -->
  <section class="panel inside-spread" aria-label="Folder inside">
    <div class="flap flap-left">
      <div class="insert insert-left">
        <div class="insert-banner" role="img" aria-label="Photo strip of caregivers with clients"><span>Harben Homecare</span><span>Harben Homecare</span></div>
        <div class="insert-brand"><span class="brand-square"></span><span>Harben</span></div>
        <p class="insert-tagline">Someone you can depend on...<br>Without question.</p>
        <div class="insert-bar"></div>
        <p class="insert-copy">Warm care at home, every day.</p>
      </div>
      <div class="pocket pocket-left">
        <div class="card-slot">business card<br>here</div>
      </div>
    </div>

    <div class="center">
      <div class="hero-photo" role="img" aria-label="Photo of a caregiver and a smiling senior man in a wheelchair raising his arms in a green park"></div>
      <p class="hero-tagline">Someone you can<br>depend on...<br>Without question.</p>
    </div>

    <div class="flap flap-right">
      <div class="insert insert-right">
        <div class="insert-head"><span class="brand-square"></span><span>Harben</span></div>
        <p class="insert-band">Someone you can depend on...<br>Without question.</p>
        <div class="insert-photo" role="img" aria-label="Photo of a caregiver with a senior couple in a flowering garden"></div>
      </div>
      <div class="pocket pocket-right">
        <div class="card-slot">business card<br>here</div>
      </div>
    </div>
  </section>

</body>
</html>
```